My product is regular Toilet Disposable Wet Wipes like the ones sold by kestrel staples

It's just athe brand of our disposable wet wipes, more information attached,

Integrate in the design the following and attached as well
- Bar code (Image attached)
- Instructions (Image attached)
- INGREDIENTS: Water, glycerin, potassium sorbate, carprylyl glycol, sodium levulinate cocoamphoacetate, tetrasodium glutamate diacetate, chamomilla recutita flower extract, citric acid.

- The wipes material used is 100% made from cellullose fiber.

- Made in China

- TALVEN WIPES COMPANY, 2417 Olsby Quarry Dr, San Diego, CA 92107, USA. T:+1.619.555.0142

Target Market(s)

All public who uses wet wipes or toilet paper

Industry/Entity Type

Meant to be sold on kestrel

Font styles to use
Other font styles liked:
• I'm open to suggestions

Colors

Designer to choose colors to be used in the design.

Requirements
Must have
• Our Brand logo and all the attachments, the pdf layout must be used
Nice to have
• I'd like a light color used reflecting hygiene, minimalistic, choose colors that go with our logo, it doesnt necesarily need to be in gold color, an option to change it is available. Same product as kestrel, yo can use that aas a reference

```html
<!DOCTYPE html>
<html lang="en">
<head>
<meta charset="utf-8">
<title>Talven Wipes – Flushable Wipes Pouch</title>
<link href="https://fonts.googleapis.com/css2?family=Lexend:wght@400;500;600&family=Montserrat:wght@400;500;600;800&display=swap" rel="stylesheet">
<style>
  :root {
    --bg: #f3f5f4;
    --green: #2db470;
    --green-deep: #0c9e55;
    --green-soft: #bfe9d2;
    --mint: #a8e4c6;
    --white: #ffffff;
    --blue: #3d6fba;
    --text-green: #2f7f50;
    --splash: #8fbfd8;
  }
  * { margin: 0; padding: 0; box-sizing: border-box; }
  html, body { width: 1200px; height: 1200px; overflow: hidden; }
  body {
    background: var(--bg);
    font-family: "Montserrat", sans-serif;
    position: relative;
  }
  .pouch {
    position: absolute;
    left: 250px; top: 100px;
    width: 700px; height: 1000px;
    border-radius: 14px;
    overflow: hidden;
    background: linear-gradient(180deg,
      var(--green) 0%, var(--green) 10%,
      #7fd6aa 24%, var(--white) 40%, var(--white) 62%,
      #8fdbb4 78%, var(--green-deep) 92%, var(--green) 100%);
  }
  .seal {
    position: absolute; left: 0; right: 0; height: 56px;
    background: repeating-linear-gradient(180deg,
      var(--green) 0 6px, var(--green-deep) 6px 8px);
  }
  .seal--top { top: 0; }
  .seal--bottom { bottom: 0; }

  .brand {
    position: absolute; top: 120px; right: 70px;
    display: flex; align-items: center; gap: 12px;
  }
  .brand__dot {
    width: 22px; height: 22px; border-radius: 50%;
    background: var(--white);
  }
  .brand__name {
    font-family: "Lexend", sans-serif; font-weight: 600;
    font-size: 30px; letter-spacing: 1px; color: var(--white);
    text-transform: uppercase;
  }

  .lid {
    position: absolute; left: 300px; top: 190px;
    width: 340px; height: 470px;
  }
  .lid svg { width: 100%; height: 100%; overflow: visible; }

  .headline {
    position: absolute; left: 60px; top: 220px;
    font-family: "Lexend", sans-serif; font-weight: 500;
    color: var(--blue); line-height: 0.95;
  }
  .headline__line { display: block; font-size: 112px; }
  .headline__line--second { padding-left: 150px; }

  .claim {
    position: absolute; left: 80px; top: 460px;
    font-family: "Lexend", sans-serif; font-weight: 400;
    color: var(--text-green); font-size: 30px; line-height: 1.2;
  }
  .claim__line--second { padding-left: 40px; }

  .splash {
    position: absolute; left: 90px; top: 560px;
    width: 380px; height: 230px;
    border-radius: 40% 60% 50% 50%;
    background: radial-gradient(ellipse at 50% 60%, var(--splash) 0%, rgba(143,191,216,0.5) 50%, rgba(143,191,216,0) 75%);
  }
  .open-tab {
    position: absolute; left: 110px; top: 700px;
    text-align: center; color: var(--text-green);
    font-size: 16px; letter-spacing: 4px;
  }
  .open-tab__arrow {
    width: 0; height: 0; margin: 0 auto 6px;
    border-left: 8px solid transparent; border-right: 8px solid transparent;
    border-bottom: 12px solid var(--text-green);
  }

  .facts {
    position: absolute; left: 60px; bottom: 150px;
    display: flex; align-items: flex-start; gap: 22px;
    color: var(--white); text-transform: uppercase;
  }
  .facts__item { padding-right: 22px; border-right: 1px solid rgba(255,255,255,0.6); }
  .facts__item:last-child { border-right: 0; }
  .count__num { font-weight: 800; font-size: 72px; line-height: 0.85; }
  .count__label { font-size: 24px; font-weight: 500; }
  .facts__text { font-size: 19px; letter-spacing: 3px; line-height: 1.25; padding-top: 6px; }
  .size {
    position: absolute; left: 60px; bottom: 100px;
    color: var(--white); font-size: 20px; letter-spacing: 1px;
  }
</style>
</head>
<body>
  <main class="pouch">
    <div class="seal seal--top"></div>

    <div class="brand">
      <span class="brand__dot"></span>
      <span class="brand__name">Talven Wipes</span>
    </div>

    <div class="lid">
      <svg viewBox="0 0 340 470">
        <path d="M40 0 H300 Q340 0 340 40 V430 Q340 470 300 470 H150 Q120 470 100 500 Q80 530 40 520 H-150 Q-180 520 -180 490 V430" fill="none" stroke="#ffffff" stroke-width="0"/>
        <rect x="0" y="0" width="340" height="470" rx="40" fill="none" stroke="#d9e3ee" stroke-width="3"/>
      </svg>
    </div>

    <h1 class="headline">
      <span class="headline__line">Flushable</span>
      <span class="headline__line headline__line--second">Wipes</span>
    </h1>

    <p class="claim">
      <span class="claim__line">No Added Dyes or Fragrance</span><br>
      <span class="claim__line claim__line--second">Fragrance Free</span>
    </p>

    <div class="splash" role="img" aria-label="Clear water splash illustration"></div>

    <div class="open-tab">
      <div class="open-tab__arrow"></div>
      OPEN
    </div>

    <div class="facts">
      <div class="facts__item count">
        <div class="count__num">42</div>
        <div class="count__label">Count</div>
      </div>
      <div class="facts__item facts__text">Sewer &amp;<br>Septic<br>Safe*</div>
      <div class="facts__item facts__text">Made with<br>Plant-Based<br>Materials</div>
    </div>
    <p class="size">6.8 IN X 5.3 IN (17.27 CM X 13.46 CM)</p>

    <div class="seal seal--bottom"></div>
  </main>
</body>
</html>
```